Business Cards

I'd like help creating business cards with the full logo "Veltrona Capital Partners" on the back of the card (navy background with white writing), and abbreviated logo "VCP" on the front. Would like to list name, title, phone number, email, and website listed on front of card. Would like to keep very simple. Front font Arial or similar.

```html
<!DOCTYPE html>
<html lang="en">
<head>
<meta charset="utf-8">
<title>Veltrona Capital Partners — Business Cards</title>
<link rel="stylesheet" href="https://fonts.googleapis.com/css2?family=Montserrat:wght@500;600&family=Arimo&display=swap">
<style>
  :root {
    --navy: #061c33;
    --white: #ffffff;
    --page: #ffffff;
    --frame: #8a96a3;
  }
  * { margin: 0; padding: 0; box-sizing: border-box; }
  html, body { width: 1010px; height: 1200px; overflow: hidden; background: var(--page); }
  .sheet {
    position: relative;
    width: 1010px;
    height: 1200px;
    border: 1px solid var(--frame);
  }
  .card {
    position: absolute;
    left: 45px;
    width: 918px;
    height: 530px;
    border-radius: 40px;
    overflow: hidden;
  }
  .card-back {
    top: 48px;
    background: var(--navy);
    border: 1px solid #000;
    display: flex;
    flex-direction: column;
    align-items: center;
    justify-content: center;
    color: var(--white);
    font-family: "Montserrat", Arial, sans-serif;
    font-weight: 600;
    padding-bottom: 40px;
  }
  .brand-name {
    font-size: 88px;
    line-height: 1;
    letter-spacing: 2px;
  }
  .brand-sub {
    margin-top: 30px;
    font-size: 38px;
    letter-spacing: 17px;
    margin-right: -17px;
  }
  .card-front {
    top: 622px;
    background: var(--white);
    border: 1.5px solid var(--navy);
  }
  .contact-band {
    position: absolute;
    left: 0;
    top: 0;
  }
  .contact-list {
    position: absolute;
    left: 0;
    top: 0;
    list-style: none;
    font-family: "Montserrat", Arial, sans-serif;
    font-weight: 500;
    color: var(--white);
    font-size: 20px;
    letter-spacing: 0.6px;
  }
  .contact-item {
    position: absolute;
    left: 12px;
    display: flex;
    align-items: center;
    white-space: nowrap;
    transform: translateY(-50%);
  }
  .contact-icon { width: 24px; height: 24px; margin-right: 16px; flex: none; }
  .monogram {
    position: absolute;
    left: 624px;
    top: 43px;
    width: 245px;
    height: 124px;
    display: flex;
    align-items: center;
    justify-content: center;
    font-family: "Montserrat", Arial, sans-serif;
    font-weight: 600;
    font-size: 96px;
    letter-spacing: 2px;
    color: var(--navy);
  }
  .person {
    position: absolute;
    left: 559px;
    width: 327px;
    top: 240px;
    text-align: center;
    font-family: "Arimo", Arial, sans-serif;
    color: var(--navy);
    line-height: 1;
  }
  .person-name { font-size: 56px; }
  .person-title { font-size: 41px; margin-top: 6px; }
  .person-rule {
    margin-top: 8px;
    height: 1.5px;
    background: var(--navy);
  }
</style>
</head>
<body>
<main class="sheet">
  <section class="card card-back" aria-label="Card back">
    <div class="brand-name">VELTRONA</div>
    <div class="brand-sub">CAPITAL PARTNERS</div>
  </section>

  <section class="card card-front" aria-label="Card front">
    <svg class="contact-band" width="530" height="530" viewBox="0 0 530 530" aria-hidden="true">
      <polygon points="0,76 330,76 519,264 330,453 0,453" fill="var(--navy)"/>
    </svg>
    <ul class="contact-list">
      <li class="contact-item" style="top:159px">
        <svg class="contact-icon" viewBox="0 0 24 24"><path fill="#fff" d="M12 1C7.6 1 4.5 4.3 4.5 8.4 4.5 13.6 12 23 12 23s7.5-9.4 7.5-14.6C19.5 4.3 16.4 1 12 1zm0 10.4a3 3 0 1 1 0-6 3 3 0 0 1 0 6z"/></svg>
        STREET NAME, STATE, COUNTRY
      </li>
      <li class="contact-item" style="top:233px">
        <svg class="contact-icon" viewBox="0 0 24 24"><path fill="#fff" d="M2 4h20v16H2zM4 7v11h16V7l-8 6z"/></svg>
        COMPANYBRAND@FREE.COM
      </li>
      <li class="contact-item" style="top:304px">
        <svg class="contact-icon" viewBox="0 0 24 24"><path fill="#fff" d="M6.6 10.8c1.4 2.8 3.8 5.2 6.6 6.6l2.2-2.2c.3-.3.7-.4 1-.2 1.1.4 2.3.6 3.6.6.6 0 1 .4 1 1V20c0 .6-.4 1-1 1C10.6 21 3 13.4 3 4c0-.6.4-1 1-1h3.5c.6 0 1 .4 1 1 0 1.3.2 2.5.6 3.6.1.3 0 .7-.2 1z"/></svg>
        522 2255 22500
      </li>
      <li class="contact-item" style="top:377px">
        <svg class="contact-icon" viewBox="0 0 24 24" fill="none" stroke="#fff" stroke-width="1.6"><circle cx="12" cy="12" r="10"/><ellipse cx="12" cy="12" rx="4.5" ry="10"/><path d="M2 12h20M4 6.5h16M4 17.5h16"/></svg>
        WWW.COMPANYNAME .COM
      </li>
    </ul>

    <div class="monogram">VCP</div>

    <div class="person">
      <div class="person-name">YOUR NAME</div>
      <div class="person-title">TITLE</div>
      <div class="person-rule"></div>
    </div>
  </section>
</main>
</body>
</html>
```